IT Professional business card with a hometown feel and a little edgy.

My business name is Tamble Website Solutions. But I have ended up doing much more. I live in a very small remote community, where everyone knows everyone. We like the one-on-one customer service in this community. I do computer tutoring, virus removal, networking, and software training. My clients are businesses and private individuals.

My website is tamblewebsitesolutions.example, when I first designed it I was going for a fresh, clean look, which I still like. But I am thinking about making the website a bit more edgy to match my new logo from ArtHively (logo attached). At this time my website does not display the new logo, but I plan on redesigning the website in the future to match the logo and business card.

My tag line is "let the internet work for you"

I'm thinking I would like to have the business card printed with a metallic finish.
Updates

Please do not use black backgrounds, or any solid dark colors. Prefer light or white backgrounds.

Target Market(s)

Small businesses. Individuals that need computer help at home.

Industry/Entity Type

It Company

Contact Information for Business Card

Nora Prandell
Tamble Website Solutions
PO Box 7153
Alderly, WA 98765
Cell: 555-271-3096
nora@tamblewebsitesolutions.example
tamblewebsitesolutions.example

Font styles to use
Serif

Requirements
Must have
• Must have all the information listed in "Business Card Details"
• Must use the logo provided.
• Use the colors from the provided logo
Nice to have
• Would like to use my tagline "let the internet work for you" all lowercase

```html
<!DOCTYPE html>
<html lang="en">
<head>
<meta charset="utf-8">
<title>Tamble Website Solutions – Business Card</title>
<link href="https://fonts.googleapis.com/css2?family=Open+Sans:wght@400;600&family=Comfortaa:wght@400&family=Questrial&display=swap" rel="stylesheet">
<style>
  :root {
    --bg: #eceeee;
    --card: #fbfbfa;
    --green-dark: #2c6a22;
    --green-light: #5f9a3c;
    --grey-text: #7b7b7b;
    --grey-dark: #3f3f3f;
    --rule: #b9b9b9;
  }
  * { margin: 0; padding: 0; box-sizing: border-box; }
  html, body { width: 1200px; height: 800px; overflow: hidden; }
  body { background: var(--bg); font-family: "Open Sans", Arial, sans-serif; }

  .card {
    position: absolute; left: 75px; top: 100px;
    width: 1050px; height: 600px;
    background: var(--card);
    box-shadow: 0 4px 18px rgba(0,0,0,.12);
  }
  .accent-bar {
    position: absolute; left: 330px; right: 40px; top: 36px;
    height: 9px; background: var(--green-dark);
  }
  .rule { position: absolute; height: 1px; background: var(--rule); }
  .rule--top { left: 30px; right: 40px; top: 112px; }
  .rule--name { left: 290px; right: 40px; top: 262px; }
  .rule--address { left: 30px; width: 360px; top: 462px; }

  .brand__mark {
    position: absolute; left: 40px; top: 150px;
    width: 74px; height: 74px; background: var(--green-light);
  }
  .brand__divider {
    position: absolute; left: 290px; top: 124px;
    width: 1px; height: 126px; background: var(--rule);
  }
  .brand__name {
    position: absolute; left: 306px; top: 140px;
    font-size: 22px; line-height: 1.12; font-weight: 400;
    color: var(--green-dark);
  }

  .person-name {
    position: absolute; right: 70px; top: 186px;
    font-size: 42px; font-weight: 400; color: var(--green-dark);
  }

  .tagline {
    position: absolute; left: 40px; top: 290px;
    font-family: "Comfortaa", "Trebuchet MS", sans-serif;
    font-size: 31px; line-height: 1.15; color: var(--grey-text);
  }

  .contact {
    position: absolute; font-family: "Questrial", Arial, sans-serif;
    font-size: 17px; line-height: 1.4; color: var(--grey-dark);
  }
  .contact svg { display: block; margin-bottom: 10px; }
  .contact--phone { left: 480px; top: 380px; }
  .contact--web { left: 680px; top: 330px; display: flex; gap: 14px; align-items: flex-start; }
  .contact--web svg { margin: 2px 0 0; }
  .contact--address { left: 40px; top: 485px; }
</style>
</head>
<body>
  <article class="card">
    <div class="accent-bar"></div>
    <div class="rule rule--top"></div>

    <div class="brand__mark"></div>
    <div class="brand__divider"></div>
    <p class="brand__name">Tamble<br>Website<br>Solutions</p>

    <h1 class="person-name">Nora Prandell</h1>
    <div class="rule rule--name"></div>

    <p class="tagline">let the internet<br>work for you!</p>

    <div class="contact contact--phone">
      <svg width="14" height="22" viewBox="0 0 14 22" aria-hidden="true">
        <rect x="1" y="1" width="12" height="20" rx="2" fill="none" stroke="#3f3f3f" stroke-width="1.6"/>
        <line x1="5" y1="17.5" x2="9" y2="17.5" stroke="#3f3f3f" stroke-width="1.4"/>
      </svg>
      <span>555-271-3096</span>
    </div>

    <div class="contact contact--web">
      <svg width="20" height="20" viewBox="0 0 20 20" aria-hidden="true">
        <g fill="none" stroke="#3f3f3f" stroke-width="1.4">
          <circle cx="10" cy="10" r="8.5"/>
          <ellipse cx="10" cy="10" rx="3.8" ry="8.5"/>
          <line x1="1.5" y1="10" x2="18.5" y2="10"/>
        </g>
      </svg>
      <span>nora@tamblewebsitesolutions.example<br>tamblewebsitesolutions.example</span>
    </div>

    <div class="rule rule--address"></div>
    <div class="contact contact--address">
      <svg width="16" height="22" viewBox="0 0 16 22" aria-hidden="true">
        <path d="M8 1a7 7 0 0 0-7 7c0 5 7 13 7 13s7-8 7-13a7 7 0 0 0-7-7z" fill="#2b2b2b"/>
        <circle cx="8" cy="8" r="2.4" fill="#fbfbfa"/>
      </svg>
      <span>PO Box 7153<br>Alderly, WA 98765</span>
    </div>
  </article>
</body>
</html>
```